Organic Label

Brightmoor Pantry grow micro greens and sprouts for the Canadian market. We need a food label for an organic "Alfalfa" sprout. We need to have English and french on the label our logo, the product name, weight, Canadian flag, UPC, keep refrigerated, pre-washed, an organic logo, postal code

Target Market(s)

Health food, Yuppies, Hipsters, Health conscious individuals ranging from 30 to 60 years

Industry/Entity Type

Health And Wellness

Colors
9bcb3c

Requirements
Must have
• We need to have English and french on the label our logo, the product name, weight, Canadian flag, UPC, keep refrigerated, pre-washed, an organic logo, postal code.
Nice to have
• Would like to see a label will a back ground look of a cardboard or rustic cotton. Not sure if that would look good but would love to see it.

```html
<!DOCTYPE html>
<html lang="en">
<head>
<meta charset="utf-8">
<title>Brightmoor Pantry – Organic Alfalfa Sprouts Label</title>
<link rel="stylesheet" href="https://fonts.googleapis.com/css2?family=Kalam:wght@400;700&family=Open+Sans:wght@400;600;700;800&display=swap">
<style>
  :root {
    --leaf-green: #6a9a3a;
    --lime: #b7cd3e;
    --cream: #f7f4d5;
    --cream-flat: #efecd6;
    --tan: #e8dfbf;
    --ribbon-red: #c8242c;
    --ink: #333333;
    --white: #ffffff;
    --page: #ffffff;
  }
  * { margin: 0; padding: 0; box-sizing: border-box; }
  html, body {
    width: 1200px; height: 532px; overflow: hidden;
    background: var(--page);
  }
  .canvas { position: relative; width: 1200px; height: 532px; }
  .label { position: absolute; top: 18px; width: 291px; height: 495px; }
  .label--wave { left: 165px; }
  .label--patch { left: 734px; }
  .label svg { display: block; width: 100%; height: 100%; }
  .script { font-family: "Kalam", cursive; }
  .sans { font-family: "Open Sans", Arial, sans-serif; }
  .brand-name { font-family: "Open Sans", Arial, sans-serif; font-weight: 600; fill: var(--leaf-green); }
</style>
</head>
<body>
<main class="canvas">

  <!-- Label variant A: sweeping green band -->
  <section class="label label--wave" aria-label="Organic alfalfa sprouts label, variant A">
    <svg viewBox="0 0 200 340" xmlns="http://www.w3.org/2000/svg">
      <defs>
        <clipPath id="wave-clip"><rect width="200" height="340"/></clipPath>
        <path id="wave-arc-outer" d="M85.5,340 A192,192 0 0 1 200,237.6"/>
        <path id="wave-arc-inner" d="M101,340 A178,178 0 0 1 200,252.4"/>
      </defs>
      <g clip-path="url(#wave-clip)">
        <rect class="label-bg" width="200" height="340" fill="var(--cream)"/>
        <path class="lower-field" d="M0,236 C70,226 150,238 200,268 L200,340 L0,340 Z" fill="var(--tan)"/>
        <path class="green-band" d="M0,140 C50,118 120,104 200,96 L200,193 C140,196 60,212 0,238 Z" fill="var(--leaf-green)"/>
        <g class="corner-stripes">
          <circle cx="260" cy="420" r="207" fill="var(--lime)"/>
          <circle cx="260" cy="420" r="203" fill="var(--leaf-green)"/>
          <circle cx="260" cy="420" r="189" fill="var(--lime)"/>
          <circle cx="260" cy="420" r="186" fill="var(--cream)"/>
          <circle cx="260" cy="420" r="174" fill="var(--lime)"/>
          <circle cx="260" cy="420" r="170" fill="var(--cream)"/>
        </g>
      </g>

      <g class="organic-seal">
        <path d="M15,0 H47 V76 L31,67 L15,76 Z" fill="var(--ribbon-red)"/>
        <circle cx="31" cy="32" r="21" fill="var(--white)" stroke="var(--leaf-green)" stroke-width="2.5"/>
      </g>

      <text class="brand-name" x="133" y="44" font-size="12.5" text-anchor="middle">Brightmoor Pantry</text>

      <text class="sans" x="155" y="88" font-size="15" font-weight="600" fill="var(--leaf-green)" text-anchor="middle">organic</text>
      <text class="script" x="127" y="148" font-size="44" fill="var(--white)" text-anchor="middle">Alfalfa</text>
      <text class="sans" x="149" y="168" font-size="14" fill="var(--ink)" text-anchor="middle">SPROUTS</text>
      <text class="sans" x="149" y="184" font-size="12" font-weight="700" fill="var(--white)" text-anchor="middle">Luzerne</text>

      <text class="sans" x="12" y="253" font-size="5" fill="var(--ink)">ingredients:</text>
      <text class="sans" x="4" y="287" font-size="4.4" font-weight="700" fill="var(--ink)">KEEP REFRIGERATED</text>
      <text class="sans" x="4" y="293" font-size="4.4" font-weight="700" fill="var(--ink)">GARDER REFRIGERATE</text>
      <rect class="code-box" x="4" y="302" width="66" height="31" fill="var(--white)"/>

      <text class="sans" font-size="9.5" font-weight="600" fill="var(--white)" letter-spacing="0.5" text-anchor="middle"><textPath href="#wave-arc-outer" startOffset="50%">PRE-WASHED</textPath></text>
      <text class="sans" font-size="7.5" font-weight="600" fill="var(--leaf-green)" text-anchor="middle"><textPath href="#wave-arc-inner" startOffset="50%">brightmoorpantry.com</textPath></text>

      <text class="sans" x="168" y="315" font-size="10" font-weight="800" fill="var(--ink)" text-anchor="end">100g</text>
      <text class="sans" x="171" y="308" font-size="3.6" font-weight="700" fill="var(--ink)">NET WT</text>
      <text class="sans" x="171" y="313" font-size="3.6" font-weight="700" fill="var(--ink)">POIDS NET</text>
      <text class="sans" x="171" y="321" font-size="4.4" fill="var(--ink)">V0N 1B4</text>
      <rect class="flag-mark" x="126" y="324" width="9" height="6" fill="var(--ribbon-red)"/>
      <text class="sans" x="138" y="330" font-size="5.5" font-weight="700" fill="var(--ink)">Grown in Canada</text>
    </svg>
  </section>

  <!-- Label variant B: green patch behind the name -->
  <section class="label label--patch" aria-label="Organic alfalfa sprouts label, variant B">
    <svg viewBox="0 0 200 340" xmlns="http://www.w3.org/2000/svg">
      <defs>
        <clipPath id="patch-clip"><rect width="200" height="340"/></clipPath>
        <path id="patch-arc-outer" d="M85.5,340 A192,192 0 0 1 200,237.6"/>
        <path id="patch-arc-inner" d="M101,340 A178,178 0 0 1 200,252.4"/>
      </defs>
      <g clip-path="url(#patch-clip)">
        <rect class="label-bg" width="200" height="340" fill="var(--cream-flat)"/>
        <path class="lower-field" d="M0,228 C70,226 150,236 200,252 L200,340 L0,340 Z" fill="var(--leaf-green)"/>
        <g class="corner-stripes">
          <circle cx="260" cy="420" r="207" fill="var(--lime)"/>
          <circle cx="260" cy="420" r="203" fill="var(--leaf-green)"/>
          <circle cx="260" cy="420" r="189" fill="var(--lime)"/>
          <circle cx="260" cy="420" r="186" fill="var(--cream-flat)"/>
          <circle cx="260" cy="420" r="174" fill="var(--lime)"/>
          <circle cx="260" cy="420" r="170" fill="var(--cream-flat)"/>
        </g>
      </g>

      <g class="organic-seal">
        <path d="M15,0 H47 V76 L31,67 L15,76 Z" fill="var(--ribbon-red)"/>
        <circle cx="31" cy="32" r="21" fill="var(--white)" stroke="var(--leaf-green)" stroke-width="2.5"/>
      </g>

      <text class="brand-name" x="135" y="44" font-size="12.5" text-anchor="middle">Brightmoor Pantry</text>

      <text class="sans" x="102" y="96" font-size="15" font-weight="700" fill="var(--leaf-green)" text-anchor="middle">organic</text>
      <rect class="name-patch" x="24" y="106" width="152" height="75" rx="4" fill="var(--leaf-green)"/>
      <text class="script" x="100" y="149" font-size="44" fill="var(--white)" text-anchor="middle">Alfalfa</text>
      <text class="sans" x="100" y="173" font-size="15" fill="var(--white)" text-anchor="middle">SPROUTS</text>
      <text class="script" x="97" y="203" font-size="17" font-weight="700" fill="var(--ink)" text-anchor="middle">Luzerne</text>

      <text class="sans" x="12" y="250" font-size="5" fill="var(--white)">ingredients:</text>
      <text class="sans" x="10" y="287" font-size="4.4" font-weight="700" fill="var(--white)">KEEP REFRIGERATED</text>
      <text class="sans" x="10" y="293" font-size="4.4" font-weight="700" fill="var(--white)">GARDER REFRIGERATE</text>
      <rect class="code-box" x="10" y="300" width="62" height="31" fill="var(--white)"/>

      <text class="sans" font-size="9.5" font-weight="600" fill="var(--white)" letter-spacing="0.5" text-anchor="middle"><textPath href="#patch-arc-outer" startOffset="50%">PRE-WASHED</textPath></text>
      <text class="sans" font-size="7.5" font-weight="600" fill="var(--leaf-green)" text-anchor="middle"><textPath href="#patch-arc-inner" startOffset="50%">brightmoorpantry.com</textPath></text>

      <text class="sans" x="168" y="315" font-size="10" font-weight="800" fill="var(--ink)" text-anchor="end">100g</text>
      <text class="sans" x="171" y="308" font-size="3.6" font-weight="700" fill="var(--ink)">NET WT</text>
      <text class="sans" x="171" y="313" font-size="3.6" font-weight="700" fill="var(--ink)">POIDS NET</text>
      <text class="sans" x="171" y="321" font-size="4.4" fill="var(--ink)">V0N 1B4</text>
      <rect class="flag-mark" x="126" y="324" width="9" height="6" fill="var(--ribbon-red)"/>
      <text class="sans" x="138" y="330" font-size="5.5" font-weight="700" fill="var(--ink)">Grown in Canada</text>
    </svg>
  </section>

</main>
</body>
</html>
```